Flint Yard Strategy Powerpoint Template

We require a powerpoint template, including an appropriate colour palette, for our marketing consultancy called "Flint Yard Strategy". We specialise in B2B Marketing & Innovation strategy for the life sciences and digital healthcare industries.
Our logo has already been designed and we have adopted two font styles for our communications so far: Bebas Neue and Bitter.
Our brand is heavily based around a contemporary industrial style and incorporates elements from east Londons design scene. In fact, our logo and brand was inspired by the street signs around flint yard in east London. Currently we use a template that uses various grey, black and off-white tones to reflect a industrial style and would like to keep clean creative innovative style. However, we are open to seeing additional colour proposals, as long as they retain the modern industrial feel.

Industry/Entity Type

Business Consultant

Colors

Designer to choose colors to be used in the design.

Requirements
Must have
• Our logo has already been designed and we have adopted two font styles for our communications so far: Bebas Neue and Bitter.
• Our brand is heavily based around a contemporary industrial style and incorporates elements from east Londons design scene. In fact, our logo and brand was inspired by the street signs around flint yard in east London.
• creative shapes and images to drop in
Nice to have
• owever, we are open to seeing additional colour proposals, as long as they retain the modern industrial feel
Should not have
• too corporate,

```html
<!DOCTYPE html>
<html lang="en">
<head>
<meta charset="UTF-8">
<title>Flint Yard Strategy — Title Slide</title>
<link rel="stylesheet" href="https://fonts.googleapis.com/css2?family=Bebas+Neue&family=Oswald:wght@200;300&display=swap">
<style>
  :root {
    --ink: #050505;
    --street-dark: #0b0b0b;
    --street-mid: #2a2a2a;
    --fog: #4a4a4a;
    --paper: #ffffff;
    --line: #f2f2f2;
  }
  html, body {
    margin: 0;
    padding: 0;
    width: 1200px;
    height: 900px;
    overflow: hidden;
    background: var(--ink);
  }
  .slide {
    position: relative;
    width: 1200px;
    height: 900px;
    overflow: hidden;
    background: var(--ink);
  }
  .slide__photo {
    position: absolute;
    inset: 0;
    background:
      radial-gradient(ellipse 260px 300px at 790px 300px, var(--fog) 0%, rgba(60,60,60,0.4) 45%, rgba(0,0,0,0) 100%),
      radial-gradient(ellipse 700px 420px at 450px 330px, var(--street-mid) 0%, rgba(20,20,20,0.6) 60%, rgba(0,0,0,0) 100%),
      linear-gradient(180deg, var(--street-dark) 0%, #1c1c1c 35%, #141414 55%, #070707 72%, var(--ink) 100%);
  }
  .title-frame {
    position: absolute;
    left: 77px;
    top: 416px;
    width: 158px;
    height: 364px;
    border: 1.5px solid var(--line);
    box-sizing: border-box;
  }
  .project-title {
    position: absolute;
    left: 176px;
    top: 460px;
    margin: 0;
    color: var(--paper);
    font-weight: normal;
  }
  .project-title__lead {
    display: block;
    font-family: "Bebas Neue", "Oswald", sans-serif;
    font-size: 80px;
    line-height: 76px;
    letter-spacing: 0.5px;
  }
  .project-title__rest {
    display: block;
    padding-top: 11px;
    font-family: "Oswald", sans-serif;
    font-weight: 200;
    font-size: 76px;
    line-height: 100px;
    text-transform: uppercase;
    letter-spacing: 8px;
  }
  .company-name {
    position: absolute;
    left: 845px;
    top: 700px;
    margin: 0;
    color: var(--paper);
    font-family: "Oswald", sans-serif;
    font-weight: 300;
    font-size: 30px;
    line-height: 40px;
    text-transform: uppercase;
    white-space: nowrap;
  }
</style>
</head>
<body>
  <main class="slide">
    <div class="slide__photo" role="img" aria-label="Black and white photograph of a foggy cobbled east London street at night, brick terraces with shop signs, a single lit street lamp and distant pedestrians"></div>

    <div class="title-frame"></div>
    <h1 class="project-title">
      <span class="project-title__lead">PROJECT</span>
      <span class="project-title__rest">Title<br>Here</span>
    </h1>

    <p class="company-name">Flint Yard Strategy</p>
  </main>
</body>
</html>
```